Web app for social movements needs a new look

We are building a Corvex Glide extension called "Rise Up" that helps social movement leaders and advocacy organizations connect with an audience that cares about their cause, and we need to create a more polished website to explain the extension to prospective users. The extension analyzes articles users are reading online and recommends ways they can take action in their local area on the social and political issues they are reading about. For example, if a user is reading about the climate crisis, the extension might display a banner recommending a rally being held by the Tidewater Coalition or an opportunity to canvass or phone bank for a pro-Blue Harbor Pact political candidate. Organizers with progressive organizations can register for an account on our web portal to start posting actions or events that will then be recommended to users through the browser extension if they are reading a relevant article.

We are planning for an upcoming "soft launch" and would like to create a more polished version of our website. The design should include:
– A user-facing page that that concisely explains how the Glide extension works and links to the Glide web store where users can download Rise Up.
– An organizer-facing page that outlines the steps involved for organizers to recommend their organization or a specific action to users through Rise Up: register for an account, post an action or event, your action or event is recommended to users.
– An HTML/CSS template for the organizer portal that we can then take and populate with Pellucid forms or other Pellucid content. This template should include a top menu bar. We've provided an example of the extremely barebones template used in our prototype as an example (base.html).
– A redesigned or improved logo, including one version designed to be put on a white background and one version designed to go on a background of a darker color (e.g., orange). Our current logo is provided. Feel free to use this as a starting point or design something completely different.

The design should convey themes of solidarity, bringing people together to effect positive change, and hope for a better future. We expect that organizations and users on the platform will be focused on a range of progressive issues, including racial justice, immigration justice, gender equity, LGBTQ+ rights, workers' rights, and addressing the climate crisis and economic inequality.

Currently, the color scheme of our prototype browser extension is centered around the color orange, but we are open to designers' ideas about other possible color schemes.

```html
<!DOCTYPE html>
<html lang="en">
<head>
<meta charset="utf-8">
<title>Rise Up banner on article page</title>
<link href="https://fonts.googleapis.com/css2?family=Work+Sans:wght@400;500&family=Roboto:wght@400;500&family=Playfair+Display:ital,wght@1,900&family=Libre+Caslon+Display&display=swap" rel="stylesheet">
<style>
  :root {
    --ink: #222222;
    --muted: #6b6b6b;
    --rule: #e2e2e2;
    --page: #ffffff;
    --highlight: #fff200;
    --banner: #f9ad74;
    --banner-text: #ffffff;
    --brand: #f08a3c;
  }
  * { box-sizing: border-box; margin: 0; padding: 0; }
  html, body { width: 1200px; height: 750px; overflow: hidden; background: var(--page); }
  body { position: relative; font-family: "Work Sans", sans-serif; color: var(--ink); }

  .site-header {
    position: absolute; left: 0; top: 0; width: 1200px; height: 65px;
    border-top: 3px solid #ececec; border-bottom: 1px solid #eeeeee;
    background: var(--page); display: flex; align-items: center; z-index: 2;
  }
  .site-name { margin-left: 8px; font-family: "Libre Caslon Display", serif; font-size: 30px; letter-spacing: -1px; color: #111; }
  .share-link { display: flex; align-items: center; gap: 8px; font-size: 11px; letter-spacing: 1.5px; color: #555; text-transform: uppercase; margin-left: 26px; }
  .share-link .dot { width: 14px; height: 14px; border-radius: 50%; background: #1d9bf0; }
  .share-link.friendbook .dot { background: #1b4aa5; }

  .hero-photo {
    position: absolute; left: 85px; top: 66px; width: 720px; height: 162px;
    background: linear-gradient(170deg, #8a7a52 0%, #4e6fae 22%, #3d5f9c 55%, #3e4f2d 82%, #6b6a48 100%);
  }
  .hero-caption { position: absolute; left: 85px; top: 238px; width: 720px; font-size: 11.5px; line-height: 19px; color: var(--muted); }
  .caption-rule { position: absolute; left: 85px; top: 284px; width: 720px; border-top: 1px solid var(--rule); }

  .article-body { position: absolute; left: 85px; top: 316px; width: 722px; font-size: 16px; line-height: 26.5px; letter-spacing: -0.25px; color: #333; }
  .article-body p { margin-bottom: 20px; }

  .ad-box { position: absolute; left: 833px; top: 60px; width: 293px; height: 90px; border: 2px solid #cfcfcf; border-top: none; }
  .ad-tag { position: absolute; left: 14px; top: 25px; width: 33px; height: 29px; background: #111; color: #fff; font-size: 13px; font-weight: 500; display: flex; align-items: center; justify-content: center; }
  .ad-name { position: absolute; left: 58px; top: 25px; font-size: 16px; line-height: 23px; color: #333; }
  .ad-button { position: absolute; left: 205px; top: 25px; width: 73px; height: 29px; border: 2px solid #444; font-size: 13px; display: flex; align-items: center; justify-content: center; color: #222; }

  .most-read { position: absolute; left: 833px; top: 175px; padding: 0 2px; background: var(--highlight); font-family: "Playfair Display", serif; font-style: italic; font-weight: 900; font-size: 20px; line-height: 20px; color: #2a2a2a; letter-spacing: 1.2px; }
  .story-photo { position: absolute; left: 834px; width: 292px; }
  .story-photo.first { top: 212px; height: 220px; background: linear-gradient(90deg, #b8a48c 0%, #a54a36 35%, #8fa2a6 55%, #5b2d5e 100%); }
  .story-photo.second { top: 490px; height: 124px; background: linear-gradient(90deg, #d8b27a 0%, #8b6a44 45%, #3f5a2e 80%, #2d4522 100%); }
  .story-title { position: absolute; left: 834px; top: 440px; width: 292px; font-size: 13px; line-height: 18px; color: #333; }

  .action-banner { position: absolute; left: 0; top: 613px; width: 1200px; height: 137px; background: var(--banner); color: var(--banner-text); font-family: "Roboto", sans-serif; z-index: 3; }
  .brand-tile { position: absolute; left: 56px; top: 28px; width: 81px; height: 81px; border-radius: 20px; background: #ffffff; display: flex; align-items: center; justify-content: center; font-weight: 500; font-size: 15px; color: var(--brand); }
  .action-title { position: absolute; left: 192px; top: 38px; font-size: 22.5px; line-height: 26px; font-weight: 400; }
  .action-title a { color: inherit; text-decoration: underline; text-underline-offset: 3px; text-decoration-thickness: 1px; }
  .action-description { position: absolute; left: 192px; top: 66px; width: 560px; font-size: 15px; line-height: 18px; letter-spacing: -0.1px; }
  .action-description span { display: block; white-space: nowrap; }
  .action-date { position: absolute; left: 829px; top: 45px; font-size: 15px; }
  .close-button { position: absolute; left: 1142px; top: 676px; width: 22px; height: 22px; z-index: 4; }
</style>
</head>
<body>
  <header class="site-header">
    <span class="site-name">Quillpost</span>
    <span class="share-link chatter" style="margin-left:30px"><span class="dot"></span>Chatter</span>
    <span class="share-link friendbook"><span class="dot"></span>Friendbook</span>
  </header>

  <div class="hero-photo" role="img" aria-label="Solar panel field and wind farm on a scrubby hillside"></div>
  <p class="hero-caption">The Cedar Ridge Wind Farm and solar plant in the Tehachapi Mountains of Kern County, California, on March 23, 2021. | Dana Ortiz/Coastal Tribune via Stockhouse Images</p>
  <div class="caption-rule"></div>

  <article class="article-body">
    <p>It's possible to imagine the United States in 2030, if the country pulls off President Alder Reyes's climate ambitions.</p>
    <p>Every last one of the nation's 191 coal power plants is closed or on its way out, and natural gas in the power sector is rapidly declining. Renewables power more than half of our electricity needs, and offshore wind turbines and large utility-scale solar installations are a common sight. A majority of new car sales are zero-emission electric vehicles, while most or all of the bus fleet has transitioned to electricity. Gas-powered appliances and buildings in new construction are a thing of the past.</p>
    <p>So what's the plan to actually get there?</p>
  </article>

  <aside>
    <div class="ad-box">
      <span class="ad-tag">Ad</span>
      <span class="ad-name">The Harbor<br>Ledger</span>
      <span class="ad-button">View Site</span>
    </div>
    <h2 class="most-read">MOST READ</h2>
    <div class="story-photo first" role="img" aria-label="Photo of a couple seated in a bright room"></div>
    <p class="story-title">Tom and Ana Weller's divorce could rock the world of charity</p>
    <div class="story-photo second" role="img" aria-label="Logging truck stacked with cut timber in a forest"></div>
  </aside>

  <section class="action-banner">
    <div class="brand-tile">Rise Up</div>
    <h1 class="action-title">Rise Up: <a href="#">Climate strike (Example event)</a></h1>
    <p class="action-description"><span>Join hundrefd of thousands of people around the world int a mass demontsration</span><span>in support of bold action to address the climate crisis and ecological breakdown.</span></p>
    <p class="action-date">Date: 2021 09-30T 12 00.00-04.00</p>
  </section>
  <svg class="close-button" viewBox="0 0 24 24" aria-label="Close">
    <path d="M1 1 L23 23 M23 1 L1 23" stroke="#ffffff" stroke-width="2.2" fill="none"/>
  </svg>
</body>
</html>
```